ちょっと急いでおりまして、
当方デザインをする時間がないので、
アウトソーシングしたいと思います。

文章、と構成だけを作りましたので、
宜しければ、お願い致します。

TAVELIA JAPAN で使用する、
お客さまにブランディングするための、
青嶺かやどり の パンフレットです。

PDFで、説明文を記載致しますので、
また見ておいて下さい。

画像素材も、添付させて頂きます。
「青嶺かやどり・かやたまご」を使うフォントは、
明朝体です。アウトラインしたデータも
添付いたします。それを活用下さい。

A4サイズ (裏・表)
両面カラーでで作っていただけると幸いです。

※もしかすると、A0サイズで引き伸ばしてつかうかもしれません。
どうぞよろしくお願い致します。

何か御不明な点がございましたら、お気軽に
ご質問ください。

当社青嶺かやどりの商品ページです。
参考にして下さい。
http://item.shopmarket-example.jp/poultry-hoshino/20004681/

青嶺かやどり協議会の ページです。
http://www.kayadori-example.com/
素材を添付いたします。レイヤーを使っておりますので、分解してください。
このページにある

の画像のような感じで、要約していただけると
幸いです。
画像を追加いたしました。
タイトルが、4Aに なってました。

すみません。A4ポスターです。
循環型の 111 のような 感じで、

ぐるっと 回る ように わかりやすく つくって頂けると幸いです。
かやどりの アニメーションデータは、

aiファイル イラストレーターの
かやたまご に 入っています。

レイヤーで組んでいますが、それを修正して作って下さい。
素材 画像を追加いたしました。
素材追加いたします。

111、222、333、444画像は、見本画像です。
イメージの参考になるかも?と思いまして、
かやどり からでる 副産物の 鶏糞堆肥もっこもこ の画像を 追加いたします。

裏側の、一番重要な情報を綺麗にまとめてくださりました。
そして、私達が やっていることに対して 共感頂けたことが大きかったです。
少し修正頂きたい部分がありますので、御連絡頂けると幸いです。

皆様 急な対応、ありがとうございます。
10件も御応募いただけるとは思っても居なかったのと、
そして、みなさんからの提案が本当に良かったので。
こちらとしても 悩ましかったです。
御提案くださった皆様。本当に、ありがとうございましたm(__)m

```html
<!DOCTYPE html>
<html lang="ja">
<head>
<meta charset="utf-8">
<title>青嶺かやどり パンフレット</title>
<link href="https://fonts.googleapis.com/css2?family=Noto+Serif+JP:wght@500;700;900&family=Zen+Maru+Gothic:wght@500;700&display=swap" rel="stylesheet">
<style>
  :root{
    --pink:#e8457e;
    --pink-soft:#f6c9d6;
    --pink-pale:#fbe6ec;
    --cream:#fdf6e8;
    --paper:#fffdf8;
    --ink:#2b2522;
    --brown:#4a3a34;
    --meat:#e9a6a0;
    --green:#6e9c3e;
    --orange:#e78a2a;
  }
  *{margin:0;padding:0;box-sizing:border-box}
  html,body{width:848px;height:1200px;overflow:hidden;background:#fff}
  body{font-family:"Zen Maru Gothic",sans-serif;color:var(--ink)}
  .poster{position:relative;width:848px;height:1200px;overflow:hidden;
    background:linear-gradient(180deg,var(--meat) 0,#f3c4bd 160px,var(--paper) 420px)}
  .abs{position:absolute}
  .vertical{writing-mode:vertical-rl}
  .photo{position:absolute;border-radius:4px}

  /* header */
  .tagline{left:300px;top:14px;width:316px;height:56px;background:#fff;border-radius:28px;
    font-size:13px;line-height:20px;text-align:center;padding-top:8px;color:var(--brown);font-weight:700}
  .tagline b{color:var(--pink)}
  .brand{left:620px;top:14px;width:214px;height:60px;background:var(--pink-pale);border:2px solid var(--pink);
    display:flex;align-items:center;gap:10px;padding-left:16px}
  .brand .dot{width:22px;height:22px;border-radius:50%;background:var(--pink)}
  .brand span{font-family:"Noto Serif JP",serif;font-weight:700;font-size:24px;color:var(--ink)}

  /* left column */
  .left-panel{left:20px;top:84px;width:306px;height:1026px;background:var(--cream);border-radius:6px}
  .flash{left:30px;top:210px;font-family:"Noto Serif JP",serif;font-weight:900;font-size:50px;line-height:54px;color:var(--pink)}
  .flash-note{left:88px;top:226px;font-size:12px;line-height:16px;color:var(--pink)}
  .bag{left:112px;top:168px;width:146px;height:240px;border-radius:10px 10px 20px 20px;
    background:linear-gradient(180deg,#f4efe2,#d9c9a4)}
  .bag-note{left:266px;top:170px;font-size:12px;color:var(--brown)}
  .compost-title{left:30px;top:420px;width:290px;font-family:"Noto Serif JP",serif;font-weight:900;font-size:33px;text-align:center;letter-spacing:1px}
  .compost-copy{left:112px;top:478px;height:240px;font-size:14px;line-height:22px;color:var(--brown)}
  .good-things{left:36px;top:580px;font-family:"Noto Serif JP",serif;font-weight:900;font-size:40px;line-height:46px;color:var(--green)}
  .cycle-head{left:256px;top:560px;font-family:"Noto Serif JP",serif;font-weight:900;font-size:34px;line-height:40px;color:var(--pink)}
  .cycle{left:24px;top:720px;width:300px;height:390px}
  .mascot-left{left:268px;top:1050px;width:52px;height:56px;border-radius:26px 26px 8px 8px;background:#f3ece7}

  /* right column */
  .headline{left:640px;top:92px;width:190px;height:300px;font-family:"Noto Serif JP",serif;font-weight:900;font-size:30px;line-height:58px}
  .headline em{font-style:normal;color:var(--pink)}
  .nature{left:420px;top:165px;width:210px}
  .nature h2{font-family:"Noto Serif JP",serif;font-weight:700;font-size:19px;line-height:28px}
  .nature h2 b{color:var(--green);font-size:25px}
  .nature p{font-size:11px;line-height:17px;margin-top:8px;color:var(--brown)}
  .farmer{left:420px;top:285px;width:272px;height:210px;background:linear-gradient(160deg,#9bb784,#cdd8b6 60%,#f0ede3)}

  .feed{left:340px;top:500px;width:508px;height:318px;background:var(--pink-soft)}
  .feed h2{position:absolute;left:100px;top:22px;font-family:"Noto Serif JP",serif;font-weight:700;font-size:22px;line-height:32px}
  .feed h2 b{color:var(--pink);font-size:28px}
  .feed p{position:absolute;left:100px;top:100px;width:220px;font-size:11px;line-height:17px;color:var(--brown)}
  .ume1{left:672px;top:595px;width:160px;height:96px;background:linear-gradient(135deg,#c05a3a,#e8b35a)}
  .ume2{left:672px;top:700px;width:160px;height:100px;background:linear-gradient(135deg,#7a2a22,#d98450)}

  .bubble{left:400px;top:830px;width:260px;height:190px}
  .bubble-text{left:500px;top:866px;height:170px;font-family:"Noto Serif JP",serif;font-weight:700;font-size:20px;line-height:34px}
  .mascot-right{left:668px;top:850px;width:172px;height:262px;border-radius:80px 80px 20px 20px;background:linear-gradient(180deg,#fffaf7,#f4e4e6)}

  /* footer */
  .footer{left:0;top:1118px;width:848px;height:82px;background:var(--brown);color:#fff;padding:14px 24px;font-size:15px;line-height:26px}
</style>
</head>
<body>
<div class="poster">

  <div class="abs tagline">おいしい <b>うれしい</b> よろこばしい。<br>みんなしあわせになりました。</div>
  <div class="abs brand"><i class="dot"></i><span>青嶺かやどり</span></div>

  <div class="abs left-panel"></div>
  <div class="abs vertical flash">速報</div>
  <div class="abs vertical flash-note">土がふかふか・野菜も元気</div>
  <div class="abs bag" role="img" aria-label="鶏糞堆肥 青嶺もっこもこ の袋のイラスト"></div>
  <div class="abs vertical bag-note">NEW</div>
  <div class="abs compost-title">発酵鶏ふん堆肥</div>
  <div class="abs vertical compost-copy">ゆっくり発酵させた堆肥は<br>畑の土をやわらかくし<br>いのちが巡る力を<br>ふたたび大地へ返します</div>
  <div class="abs vertical good-things">いいこと</div>
  <div class="abs vertical cycle-head">梅からぐるっと</div>

  <svg class="abs cycle" viewBox="0 0 300 390" aria-label="梅から巡る五つの循環">
    <circle cx="150" cy="190" r="112" fill="none" stroke="var(--pink)" stroke-width="3" stroke-dasharray="8 6"/>
    <circle cx="150" cy="190" r="62" fill="#fff" stroke="var(--pink)" stroke-width="2"/>
    <text x="150" y="180" text-anchor="middle" font-size="14" font-weight="700" fill="var(--pink)">青嶺の梅から</text>
    <text x="150" y="202" text-anchor="middle" font-size="14" font-weight="700" fill="var(--pink)">ぐるっと</text>
    <text x="150" y="222" text-anchor="middle" font-size="12" fill="var(--brown)">循環サイクル</text>
    <g font-size="12" font-weight="700" fill="var(--ink)">
      <circle cx="150" cy="78" r="20" fill="var(--pink)"/><text x="150" y="84" text-anchor="middle" fill="#fff" font-size="18">1</text>
      <text x="178" y="60">梅を育てる</text>
      <circle cx="256" cy="156" r="20" fill="var(--orange)"/><text x="256" y="162" text-anchor="middle" fill="#fff" font-size="18">2</text>
      <text x="290" y="196" text-anchor="end">梅酢を飼料に</text>
      <circle cx="216" cy="282" r="20" fill="var(--pink)"/><text x="216" y="288" text-anchor="middle" fill="#fff" font-size="18">3</text>
      <text x="216" y="320" text-anchor="middle">かやどり育つ</text>
      <circle cx="84" cy="282" r="20" fill="var(--green)"/><text x="84" y="288" text-anchor="middle" fill="#fff" font-size="18">4</text>
      <text x="84" y="320" text-anchor="middle">堆肥をつくる</text>
      <circle cx="44" cy="156" r="20" fill="var(--green)"/><text x="44" y="162" text-anchor="middle" fill="#fff" font-size="18">5</text>
      <text x="44" y="196" text-anchor="middle">畑へ還す</text>
    </g>
    <path d="M235 112 l10 -2 l-2 10" fill="none" stroke="var(--pink)" stroke-width="3"/>
    <path d="M62 110 l-2 10 l10 -2" fill="none" stroke="var(--pink)" stroke-width="3"/>
  </svg>
  <div class="abs mascot-left" role="img" aria-label="かやどりのマスコットキャラクター"></div>

  <div class="abs vertical headline"><em>かやどり</em>の<br>美味しさの秘密を、<br>細かく解説</div>

  <div class="abs nature">
    <h2><b>自然豊か</b>な環境で<br>すくすく育ちました</h2>
    <p>山あいの澄んだ空気と水に恵まれた農場で、<br>ゆったりと育てています。</p>
  </div>
  <div class="photo farmer" role="img" aria-label="農場で鶏を抱く生産者の写真"></div>

  <div class="abs feed">
    <h2><b>青嶺の梅酢</b>を<br>飼料にした贅沢な鶏</h2>
    <p>梅干しづくりで生まれる梅酢を飼料に加えました。鶏の健やかな成長を支え、肉はやわらかく旨みが豊か。臭みが少なく、さっぱりとした味わいに仕上がります。地域の恵みを無駄なく生かす、青嶺ならではの取り組みです。</p>
  </div>
  <div class="photo ume1" role="img" aria-label="梅干しを干している写真"></div>
  <div class="photo ume2" role="img" aria-label="樽に入った梅酢の写真"></div>

  <svg class="abs bubble" viewBox="0 0 260 190" aria-hidden="true">
    <path d="M30 10 H230 Q250 10 250 30 V150 Q250 170 230 170 H200 L250 186 L170 170 H30 Q10 170 10 150 V30 Q10 10 30 10Z" fill="#fff" stroke="var(--ink)" stroke-width="2"/>
  </svg>
  <div class="abs vertical bubble-text">青嶺の梅が<br>運命を変えたよ。</div>
  <div class="abs mascot-right" role="img" aria-label="かやどりのマスコットキャラクター"></div>

  <div class="abs footer">青嶺かやどり・かやたまご協議会<br>http://www.kayadori-example.com/</div>
</div>
</body>
</html>
```